Business Card design for a company called Tully Brook Co

I need a business card design for my oil fired boiler servicing company. I have a logo design already and Im just looking that incorporated into the business card design. card details; Tully Brook Co
Oil Burner Servicing - Mid Ulster Area
Service Engineer - Owen Madler
Mobile 07700914862
email - Tully.Brook.Co@quillpost.net
www.tullybrookco.net
I carry out Servicing, Commissioning, Fault Finding, Warranty Validation
Target Market(s)
home owners with oil fired central heating
Industry/Entity Type
Business
Contact Information for Business Card
Tully Brook Co
Tell. 07700914862
Web: www.tullybrookco.net
email Tully.Brook.Co@Quillpost.Net
Servicing Fault Finding Commissioning Warranty Validation
Look and feel

```html
<!DOCTYPE html>
<html lang="en">
<head>
<meta charset="utf-8">
<title>Tully Brook Co – Business Card</title>
<link rel="stylesheet" href="https://fonts.googleapis.com/css2?family=Open+Sans:wght@400;600;700&display=swap">
<style>
  :root {
    --bg: #8e8e8e;
    --card: #ffffff;
    --green: #4cb748;
    --green-deep: #3fb24a;
    --green-light: #b6d432;
    --text-white: #ffffff;
  }
  * { box-sizing: border-box; margin: 0; padding: 0; }
  html, body {
    width: 1200px; height: 900px; overflow: hidden;
    background: var(--bg);
    font-family: "Open Sans", sans-serif;
  }
  .sheet {
    width: 1200px; height: 900px;
    display: flex; flex-direction: column;
    align-items: center; justify-content: center; gap: 50px;
  }
  .card {
    position: relative;
    width: 630px; height: 360px;
    background: var(--card);
    box-shadow: 0 6px 18px rgba(0,0,0,0.25);
    overflow: hidden;
  }

  /* Front */
  .card-front { display: flex; flex-direction: column; align-items: center; justify-content: center; }
  .brand { display: flex; align-items: center; gap: 18px; }
  .brand-dot { width: 54px; height: 54px; border-radius: 50%; background: var(--green); }
  .brand-name { font-size: 48px; font-weight: 700; color: var(--green); letter-spacing: 0.5px; line-height: 1; }
  .brand-tagline {
    margin-top: 8px; margin-left: 72px;
    font-size: 11.5px; font-weight: 600; letter-spacing: 2.6px;
    color: var(--green); text-transform: uppercase;
  }
  .services { margin-top: 44px; font-size: 16px; color: var(--green); letter-spacing: 0.3px; }

  /* Back */
  .back-wave { position: absolute; inset: 0; width: 100%; height: 100%; }
  .back-brand {
    position: absolute; left: 40px; top: 0; height: 100%;
    display: flex; flex-direction: column; justify-content: center; align-items: center; gap: 16px;
    width: 240px;
  }
  .back-brand .brand-dot { width: 150px; height: 150px; }
  .back-brand .brand-name { font-size: 26px; }
  .contact {
    position: absolute; right: 44px; top: 0; height: 100%;
    text-align: right; color: var(--text-white);
  }
  .person { position: absolute; right: 0; top: 62px; white-space: nowrap; }
  .person-name { font-size: 21px; font-weight: 700; }
  .person-role { font-size: 16px; margin-top: -2px; }
  .contact-list { position: absolute; right: 0; top: 222px; list-style: none; white-space: nowrap; }
  .contact-list li {
    display: flex; align-items: center; justify-content: flex-end; gap: 8px;
    font-size: 17px; line-height: 27px;
  }
  .contact-list svg { width: 14px; height: 14px; fill: var(--text-white); }
</style>
</head>
<body>
<main class="sheet">

  <section class="card card-front">
    <div>
      <div class="brand">
        <span class="brand-dot"></span>
        <span class="brand-name">Tully Brook Co</span>
      </div>
      <p class="brand-tagline">Oil Burner Servicing - Mid Ulster Area</p>
    </div>
    <p class="services">Servicing | Fault Finding | Commissioning | Warranty Validation</p>
  </section>

  <section class="card card-back">
    <svg class="back-wave" viewBox="0 0 630 360" preserveAspectRatio="none" aria-hidden="true">
      <defs>
        <linearGradient id="wave-fill" x1="0" y1="0" x2="0" y2="1">
          <stop offset="0" stop-color="#b6d432"/>
          <stop offset="1" stop-color="#3fb24a"/>
        </linearGradient>
      </defs>
      <path d="M300 0 H630 V360 H150 C290 300 400 150 300 0 Z" fill="url(#wave-fill)"/>
      <path d="M322 10 C400 150 330 290 190 360" fill="none" stroke="#ffffff" stroke-width="2.5"/>
    </svg>

    <div class="back-brand">
      <span class="brand-dot"></span>
      <span class="brand-name">Tully Brook Co</span>
    </div>

    <div class="contact">
      <div class="person">
        <p class="person-name">Owen Madler</p>
        <p class="person-role">Service Engineer</p>
      </div>
      <ul class="contact-list">
        <li>07700914862
          <svg viewBox="0 0 24 24" aria-hidden="true"><path d="M6.6 10.8a15.1 15.1 0 0 0 6.6 6.6l2.2-2.2a1 1 0 0 1 1-.25 11.4 11.4 0 0 0 3.6.57 1 1 0 0 1 1 1V20a1 1 0 0 1-1 1A17 17 0 0 1 3 4a1 1 0 0 1 1-1h3.5a1 1 0 0 1 1 1c0 1.25.2 2.45.57 3.57a1 1 0 0 1-.25 1z"/></svg>
        </li>
        <li>Tully.Brook.Co@Quillpost.Net
          <svg viewBox="0 0 24 24" aria-hidden="true"><path d="M2 5h20v14H2z M3.5 6.5 12 13l8.5-6.5" stroke="#3fb24a" stroke-width="1.4"/></svg>
        </li>
        <li>www.tullybrookco.net
          <svg viewBox="0 0 24 24" aria-hidden="true"><circle cx="12" cy="12" r="10"/><path d="M2 12h20M12 2c3 3 3 17 0 20M12 2c-3 3-3 17 0 20" fill="none" stroke="#3fb24a" stroke-width="1.4"/></svg>
        </li>
      </ul>
    </div>
  </section>

</main>
</body>
</html>
```